Propose a revamped landing page

One template we like eg is https://www.tornavo.com but but cluttered Our logo and colors are attached to our logo and colors are printed on a white background what we have. So font usage ...
Number of Pages Required
1 page

```html
<!DOCTYPE html>
<html lang="de">
<head>
<meta charset="utf-8">
<title>Strompilot – Immer zum günstigsten Energieanbieter</title>
<link href="https://fonts.googleapis.com/css2?family=Merriweather:ital,wght@0,400;0,700;1,400&family=Montserrat:wght@500;600;700&display=swap" rel="stylesheet">
<style>
:root{
  --orange:#f7901e;
  --orange-deep:#f26522;
  --yellow:#fbb034;
  --teal:#0e8f91;
  --teal-light:#1aa7a3;
  --ink:#2b2b2b;
  --muted:#6b6b6b;
  --line:#dedede;
  --footer:#3c4147;
  --footer-deep:#2f3338;
  --white:#ffffff;
}
*{box-sizing:border-box;margin:0;padding:0}
html,body{width:1200px;height:4636px;overflow:hidden;background:var(--white)}
body{position:relative;font-family:'Merriweather',Georgia,serif;color:var(--ink)}
.abs{position:absolute}
.btn{position:absolute;display:flex;align-items:center;justify-content:center;font-family:'Montserrat',Arial,sans-serif;font-weight:700;font-size:11px;letter-spacing:.5px;text-transform:uppercase;border-radius:3px;white-space:nowrap}
.btn-fill{background:linear-gradient(90deg,var(--orange),var(--orange-deep));color:var(--white);box-shadow:0 4px 10px rgba(242,101,34,.3)}
.btn-line{border:2px solid var(--orange);color:var(--orange);background:var(--white)}
.brand{font-family:'Merriweather',Georgia,serif;font-weight:700;color:var(--orange);display:flex;align-items:center;gap:8px}
.brand-dot{width:14px;height:14px;border-radius:50%;background:var(--orange)}
.placeholder{position:absolute}
h1,h2,h3{font-weight:700}
.rule{width:60px;height:3px;background:linear-gradient(90deg,var(--orange),var(--orange-deep));margin:14px 0 20px}
.copy{font-size:13px;line-height:2;color:var(--muted)}

/* header */
.nav{position:absolute;top:50px;left:330px;width:630px;display:flex;justify-content:space-between;font-family:'Montserrat',Arial,sans-serif;font-size:10px;font-weight:600;color:#555;text-transform:uppercase;white-space:nowrap}

/* hero */
.hero-title{top:172px;left:77px;width:640px;font-size:32px;line-height:1.4}
.hero-text{top:300px;left:77px;width:560px}

/* press */
.press-title{top:592px;left:0;width:1200px;text-align:center;font-size:20px}
.press-row{top:645px;left:250px;display:flex;gap:70px}
.press-badge{width:120px;height:28px;border-radius:4px;background:#d9d9de}

/* features */
.feature-text{position:absolute}
.feature-text h2{font-size:24px;line-height:1.4}
.ticks{list-style:none;font-size:12.5px;color:var(--muted)}
.ticks li{display:flex;align-items:center;gap:14px;margin-bottom:16px}
.ticks li::before{content:"";width:16px;height:16px;border-radius:50%;background:#cfcfcf;flex:none}

/* steps */
.steps-title{top:2508px;left:160px;width:420px;text-align:center;font-size:24px}
.step-num{top:2592px;left:343px;width:44px;height:44px;border-radius:50%;background:var(--teal);color:var(--white);font-family:'Montserrat',Arial,sans-serif;font-weight:700;font-size:20px;display:flex;align-items:center;justify-content:center}
.step-name{top:2652px;left:160px;width:420px;text-align:center;font-size:16px}
.step-text{top:2696px;left:240px;width:260px;text-align:center;font-size:12px;line-height:1.9;color:var(--muted)}
.dots{top:2782px;left:345px;display:flex;gap:14px}
.dots span{width:9px;height:9px;border-radius:50%;background:#ddd}
.dots span:first-child{background:var(--orange)}

/* phone */
.phone{top:2358px;left:698px;width:285px;height:593px;border-radius:34px;background:#f1f1f3;box-shadow:0 14px 30px rgba(0,0,0,.18);padding:16px}
.phone-screen{width:100%;height:100%;border-radius:22px;background:var(--white);padding:26px 20px;position:relative}
.phone-screen .brand{font-size:19px}
.phone-menu{position:absolute;top:34px;right:22px;width:20px;height:12px;border-top:2px solid #555;border-bottom:2px solid #555}
.phone-menu::after{content:"";display:block;margin-top:3px;height:2px;background:#555}
.phone-screen h3{font-family:'Montserrat',Arial,sans-serif;font-size:20px;line-height:1.25;margin:26px 0 12px}
.phone-screen p{font-family:'Montserrat',Arial,sans-serif;font-size:12px;line-height:1.6;color:#333;font-weight:500}
.phone-link{margin-top:16px;font-family:'Montserrat',Arial,sans-serif;font-size:11px;color:var(--orange);font-weight:700;font-style:italic}
.phone-btn{margin:22px auto 0;width:190px;height:34px;border:2px solid #333;border-radius:18px;font-family:'Montserrat',Arial,sans-serif;font-size:9.5px;font-weight:700;display:flex;align-items:center;justify-content:center}
.phone-btn+.phone-btn{margin-top:12px}

/* benefits */
.section-title{position:absolute;left:0;width:1200px;text-align:center;font-size:24px}
.benefit{position:absolute;top:3183px;width:306px;height:262px;background:var(--white);box-shadow:0 6px 24px rgba(0,0,0,.1);text-align:center;padding-top:36px}
.benefit svg{display:block;margin:0 auto}
.benefit h3{font-size:17px;margin:18px 0 10px}
.benefit p{font-size:12px;line-height:1.85;color:var(--muted);padding:0 34px}

/* testimonials */
.quote{position:absolute;width:246px;background:var(--white);box-shadow:0 6px 24px rgba(0,0,0,.12);padding:80px 24px 26px}
.avatar{position:absolute;top:-40px;left:20px;width:82px;height:82px;border-radius:50%;background:radial-gradient(circle,#c9b8a8,#8c7b6e);border:4px solid var(--white)}
.quote p{font-family:'Montserrat',Arial,sans-serif;font-style:italic;font-size:12px;line-height:1.55;color:#444}
.quote strong{display:block;margin-top:22px;font-family:'Montserrat',Arial,sans-serif;font-size:11px}
.quote small{font-family:'Montserrat',Arial,sans-serif;font-size:10px;color:var(--muted)}

/* contact */
.field{position:absolute;top:4258px;width:298px;height:38px;border:1px solid var(--line);border-radius:3px;font-family:'Montserrat',Arial,sans-serif;font-size:11px;color:#999;display:flex;align-items:center;padding-left:18px}
.submit{top:4320px;left:556px;width:84px;height:32px;background:var(--teal);color:var(--white);font-size:10px}

/* footer */
.footer{top:4388px;left:0;width:1200px;height:248px;background:var(--footer)}
.footer .brand{position:absolute;top:60px;left:108px;font-size:26px}
.fcol{position:absolute;top:44px;font-family:'Montserrat',Arial,sans-serif;color:var(--white)}
.fcol h4{font-size:14px;font-weight:700;margin-bottom:20px}
.fcol a{display:block;color:#d6d6d6;font-size:10.5px;text-decoration:none;margin-bottom:14px}
.socials{display:flex;gap:10px}
.socials span{width:30px;height:30px;border-radius:50%;background:var(--white)}
.copyright{position:absolute;left:0;bottom:0;width:1200px;height:32px;background:var(--footer-deep);color:#ccc;font-family:'Montserrat',Arial,sans-serif;font-size:10px;display:flex;align-items:center;justify-content:center}
</style>
</head>
<body>

<!-- header -->
<div class="brand abs" style="top:36px;left:77px;font-size:26px">strompilot<span class="brand-dot"></span></div>
<nav class="nav"><span>Ich Stimmte Mit</span><span>Preise</span><span>Fragen</span><span>Über Uns</span><span>Betrieb</span><span>Erfahrungen</span><span>Produktdaten</span></nav>
<a class="btn btn-fill" style="top:38px;left:995px;width:123px;height:36px">Jetzt anmelden</a>

<!-- hero -->
<h1 class="abs hero-title">Immer automatisch zum günstigsten Energieanbieter wechseln</h1>
<p class="abs hero-text copy">Strompilot spart Strom jetzt anders, indem wir ständig automatisch auf den besten Energieanbieter umgestellt werden. Nutze die Preisvorteile von Strompilot und spare im Durchschnitt 425 € pro Jahr.</p>
<a class="btn btn-fill" style="top:432px;left:77px;width:130px;height:36px">Jetzt anmelden</a>
<a class="btn btn-line" style="top:432px;left:220px;width:130px;height:36px">Lern mehr</a>
<div class="placeholder" role="img" aria-label="Illustration: Energie-Inseln mit Kraftwerk, Windrädern und Häusern, verbunden durch eine Leitung" style="top:150px;left:730px;width:390px;height:375px;border-radius:40%;background:radial-gradient(circle at 45% 45%,#9fd3a6,#6fb8c9 55%,rgba(255,255,255,0) 72%)"></div>

<!-- press -->
<h2 class="abs press-title">Bekannt aus</h2>
<div class="abs press-row"><span class="press-badge"></span><span class="press-badge"></span><span class="press-badge"></span><span class="press-badge"></span></div>

<!-- feature 1 -->
<svg class="abs" style="top:695px;left:0" width="560" height="900" viewBox="0 0 560 900" aria-hidden="true">
  <defs><linearGradient id="warm" x1="0" y1="0" x2="1" y2="1"><stop offset="0" stop-color="#fbb034"/><stop offset="1" stop-color="#f26522"/></linearGradient></defs>
  <polygon points="0,0 540,250 0,895" fill="url(#warm)"/>
</svg>
<div class="placeholder" role="img" aria-label="Foto: Familie mit Kind in einem gemütlichen Wohnzimmer" style="top:933px;left:0;width:520px;height:417px;background:linear-gradient(135deg,#6b5a4a,#c9b18f 55%,#3e352e);box-shadow:0 10px 30px rgba(0,0,0,.25)"></div>
<div class="feature-text" style="top:980px;left:581px;width:520px">
  <h2>Nie wieder zu viel für Strom &amp; Gas bezahlen</h2>
  <div class="rule"></div>
  <p class="copy">Vorbei sind die Zeiten mit schlechten Deals, zeitraubendem Tarifvergleich und langwierigen Wechselprozessen.</p>
  <p class="copy" style="margin-top:14px">Mit dem automatischen Wechselservice für Strompilot wirst du nie wieder zu viel für Strom und Gas bezahlen. Und das, ohne einen Finger zu rühren. Wir kümmern uns für dich durch den Tarifdschungel.</p>
  <p class="copy" style="margin-top:14px">Also spar’ dir dein hart verdientes Geld und werde ein Strompilot.</p>
</div>
<a class="btn btn-fill" style="top:1264px;left:581px;width:130px;height:34px">Jetzt anmelden</a>

<!-- feature 2 -->
<svg class="abs" style="top:1480px;left:880px" width="320" height="920" viewBox="0 0 320 920" aria-hidden="true">
  <defs><linearGradient id="cool" x1="0" y1="0" x2="1" y2="1"><stop offset="0" stop-color="#1aa7a3"/><stop offset="1" stop-color="#0a6f7e"/></linearGradient></defs>
  <polygon points="320,0 50,250 320,250" fill="url(#cool)"/>
  <polygon points="30,661 320,661 320,900" fill="url(#cool)"/>
</svg>
<div class="placeholder" role="img" aria-label="Foto: Mann entspannt mit Laptop auf einem Sofa vor einer Stadtkulisse" style="top:1730px;left:624px;width:576px;height:411px;background:linear-gradient(160deg,#b9cfdc,#6f8fa3 50%,#2c3a44)"></div>
<div class="feature-text" style="top:1780px;left:132px;width:460px">
  <h2>Die günstigste aller Superkräfte</h2>
  <div class="rule"></div>
  <p style="font-size:14px;font-weight:700;margin-bottom:20px">Ab 24 Euro bist du</p>
  <ul class="ticks">
    <li>Service für Strom oder Gas (1 Zähler): 24 Euro/Jahr</li>
    <li>Service für Strom und Gas (2 Zähler): 36 Euro/Jahr</li>
    <li>Die erste Gebühr verrechnen wir mit dem nächsten Wechsel</li>
    <li>Spare bis zu 850 Euro jährlich Strom- und Gaskosten beim 1. Wechsel*</li>
  </ul>
</div>
<a class="btn btn-fill" style="top:2065px;left:132px;width:130px;height:34px">Jetzt anmelden</a>

<!-- steps -->
<h2 class="abs steps-title">Wie werde ich Strompilot?</h2>
<svg class="abs" style="top:2640px;left:158px" width="16" height="24" viewBox="0 0 16 24" aria-hidden="true"><polyline points="12,2 3,12 12,22" fill="none" stroke="#bbb" stroke-width="2"/></svg>
<svg class="abs" style="top:2640px;left:560px" width="16" height="24" viewBox="0 0 16 24" aria-hidden="true"><polyline points="4,2 13,12 4,22" fill="none" stroke="#bbb" stroke-width="2"/></svg>
<div class="abs step-num">1</div>
<h3 class="abs step-name">Einmalig anmelden</h3>
<p class="abs step-text">Jahresrechnung hochladen. Präferenzen auswählen. Anmeldung abschließen.</p>
<div class="abs dots"><span></span><span></span><span></span></div>

<div class="abs phone">
  <div class="phone-screen">
    <div class="brand">strompilot<span class="brand-dot" style="width:10px;height:10px"></span></div>
    <div class="phone-menu"></div>
    <h3>Willkommen bei der Anmeldung</h3>
    <p>Du bist nur wenige Klicks davon entfernt, Strompilot zu werden. Das bedeutet: nie wieder zu viel für Strom &amp; Gas zu bezahlen! Denn mit unserem automatischen Energieanbieter-Wechselservice wechselst du jedes Jahr deinen Energieanbieter und sparst dir durch attraktive Rabatte eine ganze Menge Geld– ohne einen Finger zu rühren!</p>
    <div class="phone-link">Hast du deine Jahresrechnung dabei?</div>
    <div class="phone-btn">JA, WEITER ANMELDEN</div>
    <div class="phone-btn">NEIN, ICH MUSS SIE ERST SUCHEN</div>
  </div>
</div>

<!-- benefits -->
<h2 class="section-title" style="top:3082px">Einmal anmelden, immer sparen</h2>
<div class="benefit" style="left:99px">
  <svg width="56" height="56" viewBox="0 0 56 56" aria-hidden="true"><circle cx="28" cy="28" r="24" fill="none" stroke="#333" stroke-width="2.5"/><polyline points="16,29 25,38 41,19" fill="none" stroke="#f7901e" stroke-width="3"/></svg>
  <h3>Unabhängig</h3>
  <p>Wir arbeiten nur für dich. Uns unabhängig zu bleiben, verzichten wir bewusst auf Provisionen deals mit Energieanbietern.</p>
</div>
<div class="benefit" style="left:448px">
  <svg width="56" height="56" viewBox="0 0 56 56" aria-hidden="true"><rect x="6" y="10" width="44" height="40" rx="3" fill="none" stroke="#333" stroke-width="2.5"/><line x1="6" y1="20" x2="50" y2="20" stroke="#333" stroke-width="2.5"/><circle cx="28" cy="35" r="9" fill="none" stroke="#f7901e" stroke-width="2.5"/><polyline points="28,30 28,35 32,37" fill="none" stroke="#f7901e" stroke-width="2"/></svg>
  <h3>Automatisch</h3>
  <p>Du meldest dich einmal an und wir übernehmen den Rest. Ganz automatisch.</p>
</div>
<div class="benefit" style="left:797px">
  <svg width="56" height="56" viewBox="0 0 56 56" aria-hidden="true"><rect x="6" y="14" width="44" height="30" rx="3" fill="none" stroke="#333" stroke-width="2.5"/><circle cx="28" cy="29" r="8" fill="#f7901e"/></svg>
  <h3>Fair</h3>
  <p>Strompilot verdient nicht bei Wechsel. Transparent Service-Gebühr.</p>
</div>

<!-- testimonials -->
<h2 class="section-title" style="top:3576px">Client Testimonials</h2>
<svg class="abs" style="top:3755px;left:0" width="1200" height="340" viewBox="0 0 1200 340" aria-hidden="true">
  <defs><linearGradient id="band" x1="0" y1="0" x2="1" y2="0"><stop offset="0" stop-color="#0a6f7e"/><stop offset="1" stop-color="#1aa7a3"/></linearGradient></defs>
  <polygon points="0,70 1200,0 1200,340 0,340" fill="url(#band)"/>
</svg>
<div class="quote" style="top:3708px;left:164px">
  <div class="avatar" role="img" aria-label="Porträtfoto eines Kunden"></div>
  <p>Proin ac quam et lectus vestibulum blandit. Nunc maximus nibh at placerat tincidunt. Nam sem lacus, ornare non ante sed, ultricies fringilla massa. Ut congue, elit non tempus elementum, sem risus tincidunt diam.</p>
  <strong>Jonas Berger</strong><small>Berlin, Germany</small>
</div>
<div class="quote" style="top:3662px;left:488px">
  <div class="avatar" role="img" aria-label="Porträtfoto eines Kunden"></div>
  <p>Proin ac quam et lectus vestibulum blandit. Nunc maximus nibh at placerat tincidunt. Nam sem lacus, ornare non ante sed, ultricies fringilla massa. Ut congue, elit non tempus elementum.</p>
  <strong>Lukas Brandt</strong><small>Berlin, Germany</small>
</div>
<div class="quote" style="top:3708px;left:810px">
  <div class="avatar" role="img" aria-label="Porträtfoto einer Kundin"></div>
  <p>Proin ac quam et lectus vestibulum blandit. Nunc maximus nibh at placerat tincidunt. Nam sem lacus, ornare non ante sed, ultricies fringilla massa. Ut congue, elit non tempus elementum, sem risus tincidunt diam.</p>
  <strong>Clara Weiss</strong><small>Berlin, Germany</small>
</div>

<!-- contact -->
<h2 class="section-title" style="top:4186px">Habe Fragen ?</h2>
<div class="field" style="left:284px">Enter your Postal code</div>
<div class="field" style="left:612px">Enter your Email</div>
<a class="btn submit">Submit</a>

<!-- footer -->
<footer class="abs footer">
  <div class="brand" style="color:var(--orange)">strompilot<span class="brand-dot"></span></div>
  <div class="fcol" style="left:315px"><h4>Company</h4><a>About Us</a><a>Contact Us</a></div>
  <div class="fcol" style="left:470px"><h4>Learn &amp; Support</h4><a>How it works</a><a>Energy Guides</a><a>FAQs</a></div>
  <div class="fcol" style="left:667px"><h4>Legal</h4><a>Terms and Conditions</a><a>Privacy Policy</a><a>Cookies</a><a>Contact Us</a></div>
  <div class="fcol" style="left:853px"><h4>Follow us</h4><div class="socials"><span></span><span></span><span></span><span></span><span></span></div></div>
  <div class="copyright">© Strompilot. All rights reserved</div>
</footer>

</body>
</html>
```